Website Design for Business Law Firm

We have a logo and now we would like a web site design for our new website. Our small firm provides creative and aggressive transactional (not litigation) legal services to advise healthcare, technology, internet-based and traditional companies and investors in such companies on healthcare, technology, financing, mergers/acquisitions, real estate and other transactions, legal compliance and general corporate and business matters.

We would like to see a website design that is professional and appropriate for executives, professionals, investors and government regulators to visit, that conveys professionalism and competence while being a little edgy and modern - no typical legal motifs such as gavels, books, or scales of justice. We advise businesses and investors and guide them through complicated issues quickly, capably and differently from other law firms. We are part of the business team and get things done.

The logo is attached, and we like gray as a color to complement it. The intention of the logo is to convey that in a storm or challenging time, people come to this firm, and people come to this firm when they need the power and disruption to change things or shake them up.

I have also enclosed a picture of our business card for consideration.

On the other hand, you can check out the current simple site at www.quenlow.example to see we have used a space motif in the past to evoke that we help create stars (the nebula featured there). This is not a necessary part of the new website and it may look better without it.

We appreciate your creativity and look forward to designs.

Industry/Entity Type

Business

Requirements
Must have
• We anticipate the following pages, and you may submit different ideas for the different pages:
• 1. Landing page
• 2. Services pages - healthcare, IT/Technology, general counsel services, financings, mergers/acquisitions, mediation/arbitration, procurement and productization
• 3. About Us including contact information
• Our name and contact information:
• Quenlow Law Firm, P.C.
• 7816 SW 19th Ave.
• Portland, OR 97213
• phone: 555.614.2873
• fax: 555.730.4158
Nice to have
• Please consider designs that enhance the impressions we are looking for
Should not have
• Please no gavels, scales of justice, law books, or similar traditional legal imagery.

```html
<!DOCTYPE html>
<html lang="en">
<head>
<meta charset="utf-8">
<title>Quenlow Law Firm</title>
<link href="https://fonts.googleapis.com/css2?family=Ubuntu:wght@400;500;700&family=Fjalla+One&family=Arimo:wght@400;700&display=swap" rel="stylesheet">
<style>
:root{
  --page:#dcdcdc;
  --white:#ffffff;
  --teal:#4e6a6e;
  --teal-dark:#3f585c;
  --ink:#2b2b2b;
  --text:#3a3a3a;
  --rule:#cfcfcf;
  --field:#ececec;
  --footer:#4a4a4a;
  --footer-text:#e8e8e8;
}
*{box-sizing:border-box;margin:0;padding:0}
html,body{width:1020px;height:1200px;overflow:hidden}
body{background:var(--page);font-family:"Arimo",Arial,sans-serif;color:var(--text);position:relative}
.sheet{position:absolute;left:111px;top:0;width:798px;height:1052px;background:var(--white)}
.abs{position:absolute}
.brand{left:120px;top:12px;width:262px;height:64px;display:flex;align-items:center;gap:10px}
.brand-mark{width:22px;height:22px;background:var(--teal)}
.brand-name{font-family:"Ubuntu",sans-serif;font-weight:700;font-size:38px;letter-spacing:4px;color:var(--ink)}
.top-phone{right:117px;top:23px;display:flex;align-items:center;gap:6px;font-family:"Ubuntu",sans-serif;font-weight:500;font-size:17px;color:var(--text);letter-spacing:.5px}
.top-phone .ico{width:24px;height:24px;background:var(--teal);border-radius:3px;display:flex;align-items:center;justify-content:center}
.top-email{right:117px;top:53px;font-size:12px;font-weight:700;color:var(--text)}
.nav{left:120px;top:90px;width:781px;height:36px;background:linear-gradient(#6e8a8d,#4a6669);display:flex}
.nav a{display:flex;align-items:center;justify-content:center;color:#fff;font-family:"Ubuntu",sans-serif;font-weight:500;font-size:12px;text-decoration:none;border-right:1px solid #3d5558;box-shadow:inset -1px 0 0 #7d9699}
.nav a.active{background:linear-gradient(#8ea3a5,#6d8689)}
.nav a:last-child{border-right:none;box-shadow:none}
.hero{left:120px;top:134px;width:781px;height:334px;background:#c9c9c9;padding:4px}
.hero-photo{width:100%;height:100%;background:linear-gradient(100deg,#2b3446 0%,#8f9aa8 30%,#d9dde2 50%,#7e8ea3 70%,#263349 100%);position:relative}
.hero-caption{position:absolute;left:17px;bottom:10px;font-family:"Fjalla One",sans-serif;font-size:29px;color:#fff;text-shadow:1px 1px 3px rgba(0,0,0,.7)}
.dots{position:absolute;right:14px;bottom:14px;display:flex;gap:4px}
.dots span{width:11px;height:11px;border-radius:50%;background:#111;border:1px solid #fff}
.dots span.on{background:#fff;border-color:#111}
h2{font-family:"Ubuntu",sans-serif;font-weight:500;font-size:19px;color:var(--ink)}
h2 em{font-style:normal;color:var(--teal)}
.welcome{left:121px;top:481px;width:530px}
.welcome h2{border-bottom:1px solid var(--rule);padding-bottom:4px;width:526px}
.welcome p{font-size:9.6px;line-height:15.3px;margin-top:6px;color:var(--text)}
.welcome p+p{margin-top:8px}
.read-more{right:0;top:150px;font-size:10px;font-weight:700;color:var(--ink)}
.vrule{left:670px;top:490px;width:1px;height:140px;background:#eee}
.quick{left:689px;top:481px;width:212px}
.quick h2{border-bottom:1px solid var(--rule);padding-bottom:4px}
.field{position:absolute;left:-1px;width:213px;background:var(--field);border:1px solid #cfcfcf;border-radius:3px;font-size:10px;color:#444;padding:5px 7px}
.submit{position:absolute;left:-1px;top:148px;width:58px;height:18px;background:linear-gradient(#666,#2e2e2e);color:#fff;font-size:10px;font-weight:700;display:flex;align-items:center;justify-content:center;border-radius:2px}
.card{top:671px;width:249px;height:216px;background:#f7f7f7;border:1px solid #d2d2d2;border-radius:4px;overflow:hidden}
.card-head{height:30px;background:var(--teal);color:#fff;font-family:"Ubuntu",sans-serif;font-weight:500;font-size:18px;letter-spacing:1px;text-align:center;line-height:31px;position:relative}
.card-head::after{content:"";position:absolute;right:20px;bottom:-9px;border-left:10px solid transparent;border-right:10px solid transparent;border-top:9px solid var(--teal)}
.corner{position:absolute;right:0;bottom:0;width:36px;height:36px;background:linear-gradient(135deg,transparent 50%,var(--teal) 50%)}
.corner::after{content:"+";position:absolute;right:4px;bottom:-1px;color:#fff;font-weight:700;font-size:16px}
.who-photo{position:absolute;left:10px;top:45px;width:226px;height:106px;border-radius:4px;background:linear-gradient(90deg,#3d4a5c,#b9c3cc 50%,#e4e6e8 70%,#4a4037)}
.card p{font-size:9.6px;line-height:13.5px;color:var(--text)}
.who-text{position:absolute;left:10px;top:158px;width:230px}
.svc-text{position:absolute;left:15px;top:44px;width:225px}
.svc-list{position:absolute;left:25px;top:88px;list-style:none}
.svc-list li{font-size:10.2px;font-weight:700;color:var(--ink);height:21px;display:flex;align-items:center;gap:7px;letter-spacing:.3px}
.news-item{position:absolute;left:13px;width:222px;display:flex;gap:8px;padding-bottom:8px;border-bottom:1px dotted #c8c8c8}
.news-item:last-of-type{border-bottom:none}
.news-item b{display:block;font-size:10.2px;color:var(--ink)}
.testi{left:121px;top:904px;width:778px}
.testi h2{border-bottom:1px solid var(--rule);padding-bottom:4px}
.quote{position:absolute;top:36px;width:240px;height:80px}
.quote .mark{position:absolute;left:0;top:-6px;font-family:Georgia,serif;font-size:34px;color:#8b9da0;font-weight:700}
.quote p{margin-left:24px;font-size:9.8px;line-height:15px}
.quote .who{position:absolute;left:22px;top:60px;font-size:10px;font-weight:700;color:var(--teal-dark);letter-spacing:.3px}
.qrule{position:absolute;top:36px;width:1px;height:75px;background:#ccc}
.pager{left:860px;top:1022px;width:41px;height:15px;border:1px solid #ccc;border-radius:2px;display:flex}
.pager span{flex:1;display:flex;align-items:center;justify-content:center;font-size:7px;color:#999}
.pager span+span{border-left:1px solid #ccc}
.footer{position:absolute;left:0;top:1052px;width:1020px;height:148px;background:var(--footer);color:var(--footer-text)}
.fcol{position:absolute;top:14px}
.fcol h3{font-family:"Ubuntu",sans-serif;font-weight:500;font-size:14.5px;color:#fff;letter-spacing:.5px;border-bottom:1px solid #5e5e5e;padding-bottom:6px}
.fsep{position:absolute;top:14px;width:1px;height:120px;background:#404040;box-shadow:1px 0 0 #575757}
.link-cols{display:flex}
.links{list-style:none;font-size:10.4px;line-height:16.8px;margin-top:6px;white-space:nowrap}
.links:first-child{width:69px}
.links li::before{content:"» ";font-size:7px;color:#aaa;vertical-align:1px}
.fcol p{font-size:10.4px;line-height:13.7px}
.subscribe-field{width:157px;height:20px;background:#fff;border-radius:3px;color:#555;font-size:10px;padding:3px 10px;margin-top:10px}
.subscribe{display:inline-block;margin-top:6px;background:#2a2a2a;color:#fff;font-size:9.6px;font-weight:700;padding:3px 7px;border:1px solid #666;border-radius:2px}
.crow{display:flex;gap:8px;align-items:flex-start;margin-top:8px;font-size:10.2px;line-height:15px}
.social{display:flex;gap:5px;justify-content:center;margin-top:16px}
.social span{width:22px;height:22px;border-radius:3px;background:#6f8a8e}
.copy{text-align:center;font-size:10.4px;line-height:16px;margin-top:10px}
</style>
</head>
<body>
<div class="sheet"></div>

<header>
  <div class="abs brand"><span class="brand-mark"></span><span class="brand-name">QUENLOW</span></div>
  <div class="abs top-phone"><span class="ico"><svg width="13" height="13" viewBox="0 0 24 24"><path fill="#fff" d="M6.6 10.8a15 15 0 0 0 6.6 6.6l2.2-2.2c.3-.3.7-.4 1-.2 1.1.4 2.3.6 3.6.6.6 0 1 .4 1 1V20c0 .6-.4 1-1 1C10.6 21 3 13.4 3 4c0-.6.4-1 1-1h3.5c.6 0 1 .4 1 1 0 1.3.2 2.5.6 3.6.1.3 0 .7-.2 1z"/></svg></span>555 614 2873</div>
  <div class="abs top-email">Email: info@quenlow.example</div>
  <nav class="abs nav">
    <a class="active" style="width:96px">Home</a>
    <a style="width:111px">Our Firm</a>
    <a style="width:108px">Services</a>
    <a style="width:121px">Resources</a>
    <a style="width:129px">Case Studies</a>
    <a style="width:95px">News</a>
    <a style="width:121px">Contact Us</a>
  </nav>
</header>

<section class="abs hero">
  <div class="hero-photo" role="img" aria-label="Photo of three business professionals reviewing documents in a bright office">
    <div class="hero-caption">Pragmatic, Creative Services For Innovative Businesses</div>
    <div class="dots"><span class="on"></span><span></span><span></span><span></span></div>
  </div>
</section>

<section class="abs welcome">
  <h2>Welcome to <em>Quenlow</em></h2>
  <p>Lorem ipsum dolor sit amet, consectetur adipisicing elit, sed do eiusmod tempor incididunt ut labore et dolore magaingna aliqua. Ut enim ad minim veniam, quis nostrud exercitation ullamco laboris nisi ut aliquip ex ea commodo consequat Duis aute irure dolor in reprehenderit in voluptate velit esse cillum dolore eu fugiat nulla pariatur. Excepteur sint occae cupidatat non proident, sunt in culpa qui officia deserunt mollit anim id est laborum.</p>
  <p>Lorem ipsum dolor sit amet, consectetur adipisicing elit, sed do eiusmod tempor incididunt ut labore et dolore magaingna aliqua. Ut enim ad minim veniam, quis nostrud exercitation ullamco laboris nisi ut aliquip ex ea commodo consequat Duis aute irure dolor in reprehenderit in voluptate velit esse cillum dolore eu fugiat nulla pariatur.</p>
  <div class="abs read-more">Read More »</div>
</section>
<div class="abs vrule"></div>

<section class="abs quick">
  <h2>Quick <em>Contact</em></h2>
  <div class="field" style="top:34px;height:20px">Name</div>
  <div class="field" style="top:59px;height:20px">Email</div>
  <div class="field" style="top:84px;height:55px">Message</div>
  <div class="submit">SUBMIT</div>
</section>

<section class="abs card" style="left:120px">
  <div class="card-head">Who We Are</div>
  <div class="who-photo" role="img" aria-label="Photo of colleagues discussing papers at a meeting table"></div>
  <p class="who-text">Lorem ipsum dolor sit amet, conseuer adipiscing ut laoreet dolore magna aliquam erat volutpa wisi enim ad minim veniam</p>
  <span class="corner"></span>
</section>

<section class="abs card" style="left:386px">
  <div class="card-head">Services</div>
  <p class="svc-text">legal services to advise healthcare, technology, internet-based and traditional companies and investors in such companies on</p>
  <ul class="svc-list">
    <li><svg width="10" height="9" viewBox="0 0 10 9"><path d="M0 4.5h8M5 1l3.5 3.5L5 8" stroke="#333" stroke-width="1.6" fill="none"/></svg>Healthcare</li>
    <li><svg width="10" height="9" viewBox="0 0 10 9"><path d="M0 4.5h8M5 1l3.5 3.5L5 8" stroke="#333" stroke-width="1.6" fill="none"/></svg>Technology</li>
    <li><svg width="10" height="9" viewBox="0 0 10 9"><path d="M0 4.5h8M5 1l3.5 3.5L5 8" stroke="#333" stroke-width="1.6" fill="none"/></svg>Financing</li>
    <li><svg width="10" height="9" viewBox="0 0 10 9"><path d="M0 4.5h8M5 1l3.5 3.5L5 8" stroke="#333" stroke-width="1.6" fill="none"/></svg>Mergers/acquisitions</li>
    <li><svg width="10" height="9" viewBox="0 0 10 9"><path d="M0 4.5h8M5 1l3.5 3.5L5 8" stroke="#333" stroke-width="1.6" fill="none"/></svg>Real estate</li>
  </ul>
  <span class="corner"></span>
</section>

<section class="abs card" style="left:652px">
  <div class="card-head">Latest News</div>
  <div class="news-item" style="top:44px">
    <svg width="19" height="20" viewBox="0 0 19 20"><rect x="1" y="3" width="17" height="16" fill="none" stroke="#777" stroke-width="1.4"/><rect x="1" y="3" width="17" height="4" fill="#777"/><path d="M5 1v4M14 1v4" stroke="#777" stroke-width="1.6"/><g fill="#888"><rect x="4" y="9" width="2" height="2"/><rect x="8.5" y="9" width="2" height="2"/><rect x="13" y="9" width="2" height="2"/><rect x="4" y="13" width="2" height="2"/><rect x="8.5" y="13" width="2" height="2"/><rect x="13" y="13" width="2" height="2"/></g></svg>
    <p><b>Lorem ipsum sit amet consectetur</b>sicinge elitsed do eiusmod tempor inciil laborei et dolore magna aliqua.</p>
  </div>
  <div class="news-item" style="top:101px">
    <svg width="19" height="20" viewBox="0 0 19 20"><rect x="1" y="3" width="17" height="16" fill="none" stroke="#777" stroke-width="1.4"/><rect x="1" y="3" width="17" height="4" fill="#777"/><path d="M5 1v4M14 1v4" stroke="#777" stroke-width="1.6"/><g fill="#888"><rect x="4" y="9" width="2" height="2"/><rect x="8.5" y="9" width="2" height="2"/><rect x="13" y="9" width="2" height="2"/><rect x="4" y="13" width="2" height="2"/><rect x="8.5" y="13" width="2" height="2"/><rect x="13" y="13" width="2" height="2"/></g></svg>
    <p><b>Ut wisi enim ad minim nostrud</b>exerci tation ullamcorpe suscipit lobortis nisl ut aliquip e ea commod.</p>
  </div>
  <div class="news-item" style="top:156px">
    <svg width="19" height="20" viewBox="0 0 19 20"><rect x="1" y="3" width="17" height="16" fill="none" stroke="#777" stroke-width="1.4"/><rect x="1" y="3" width="17" height="4" fill="#777"/><path d="M5 1v4M14 1v4" stroke="#777" stroke-width="1.6"/><g fill="#888"><rect x="4" y="9" width="2" height="2"/><rect x="8.5" y="9" width="2" height="2"/><rect x="13" y="9" width="2" height="2"/><rect x="4" y="13" width="2" height="2"/><rect x="8.5" y="13" width="2" height="2"/><rect x="13" y="13" width="2" height="2"/></g></svg>
    <p><b>Lorem ipsum sit amet consectetur</b>sicinge elitsed do eiusmod tempor incidil laborei et dolore magna aliqua.</p>
  </div>
  <span class="corner"></span>
</section>

<section class="abs testi">
  <h2>Client <em>Testimonials</em></h2>
  <div class="quote" style="left:0"><span class="mark">“</span><p>Lorem ipsum dolor sit amet co adipisic elitsed do eiusmod tempor incididunt labore et dolore magna aliqua. Ut ad mi veniam, quis nostrud</p><span class="who">-Mr.client Name, Location</span></div>
  <div class="qrule" style="left:253px"></div>
  <div class="quote" style="left:270px"><span class="mark">“</span><p>Lorem ipsum dolor sit amet co adipisic elitsed do eiusmod tempor incididunt labore et dolore magna aliqua. Ut ad mi veniam, quis nostrud</p><span class="who">-Mr.client Name, Location</span></div>
  <div class="qrule" style="left:522px"></div>
  <div class="quote" style="left:538px"><span class="mark">“</span><p>Lorem ipsum dolor sit amet co adipisic elitsed do eiusmod tempor incididunt labore et dolore magna aliqua. Ut ad mi veniam, quis nostrud</p><span class="who">-Mr.client Name, Location</span></div>
</section>
<div class="abs pager"><span>◀</span><span>▶</span></div>

<footer class="footer">
  <div class="fcol" style="left:119px;width:131px">
    <h3>Quick Links</h3>
    <div class="link-cols">
      <ul class="links"><li>Home</li><li>Our Firm</li><li>Services</li><li>Resources</li><li>Case Studies</li></ul>
      <ul class="links"><li>News</li><li>Contact Us</li></ul>
    </div>
  </div>
  <div class="fsep" style="left:272px"></div>
  <div class="fcol" style="left:299px;width:160px">
    <h3>Newsletter</h3>
    <p style="margin-top:7px;padding-left:2px">Get the latest updates by entering your email address</p>
    <div class="subscribe-field">Email Address</div>
    <span class="subscribe">Subscribe</span>
  </div>
  <div class="fsep" style="left:482px"></div>
  <div class="fcol" style="left:514px;width:182px">
    <h3>Contact Details</h3>
    <div class="crow"><svg width="11" height="15" viewBox="0 0 11 15"><path d="M5.5 0A5.5 5.5 0 0 0 0 5.5C0 9.5 5.5 15 5.5 15S11 9.5 11 5.5A5.5 5.5 0 0 0 5.5 0zm0 7.7a2.2 2.2 0 1 1 0-4.4 2.2 2.2 0 0 1 0 4.4z" fill="#eee"/></svg><span>Quenlow Law Firm, P.C., P.O. Box 6152, Portland, OR 97213</span></div>
    <div class="crow"><svg width="11" height="11" viewBox="0 0 24 24"><path fill="#eee" d="M6.6 10.8a15 15 0 0 0 6.6 6.6l2.2-2.2c.3-.3.7-.4 1-.2 1.1.4 2.3.6 3.6.6.6 0 1 .4 1 1V20c0 .6-.4 1-1 1C10.6 21 3 13.4 3 4c0-.6.4-1 1-1h3.5c.6 0 1 .4 1 1 0 1.3.2 2.5.6 3.6.1.3 0 .7-.2 1z"/></svg><span>555 614 2873</span></div>
    <div class="crow" style="margin-top:4px"><svg width="13" height="10" viewBox="0 0 13 10"><rect x=".5" y=".5" width="12" height="9" fill="none" stroke="#eee"/><path d="M.5.5l6 5 6-5" stroke="#eee" fill="none"/></svg><span>info@quenlow.example</span></div>
  </div>
  <div class="fsep" style="left:721px"></div>
  <div class="fcol" style="left:754px;width:147px">
    <h3>Follow Us</h3>
    <div class="social"><span></span><span></span><span></span><span></span></div>
    <div class="copy">Copyright © 2013 Quenlow.<br>All Rights Reserved</div>
  </div>
</footer>
</body>
</html>
```